Business Card Design Project

We are looking for a new business card design for a Drilling company in WA, Australia.

We are in between offices, however require a design in the meantime due to some upcoming events with our basic information.

The Logo for our company is Blue and Grey and would like this colour scheme throughout.

We are quite a new company so would like a memorable design that stands out and communicates a strong commitment to safety, quality of work and performance.

The company name is Ironbark Boring Group (IBG)

The details to be included are as follows:

Gavin Thorley
Managing Director
m.0481639207
e.gavin@ibgpty.com.au

Martin Thorley
Director
m.0419852637
e.martin@ibgpty.com.au

Industry/Entity Type

Events

Requirements
Must have
• Under the Logo, we would like 'Western Australia'

```html
<!DOCTYPE html>
<html lang="en">
<head>
<meta charset="utf-8">
<title>Ironbark Boring Group – Business Cards</title>
<link rel="stylesheet" href="https://fonts.googleapis.com/css2?family=Raleway:wght@400;600;700&family=Dosis:wght@500;600;700&display=swap">
<style>
  :root {
    --page-bg: #ffffff;
    --card-dark: #1c1c1e;
    --card-dark-edge: #141415;
    --divider-grey: #8a8c8f;
    --brand-blue: #1f3f8f;
    --brand-blue-deep: #1a3577;
    --brand-grey: #8f9194;
    --tagline-blue: #4a6fc4;
    --text-light: #ffffff;
    --text-soft: #d9e0f0;
  }
  * { box-sizing: border-box; margin: 0; padding: 0; }
  html, body {
    width: 1200px;
    height: 900px;
    overflow: hidden;
    background: var(--page-bg);
  }
  .canvas {
    position: relative;
    width: 1200px;
    height: 900px;
    display: flex;
    flex-direction: column;
    align-items: center;
    justify-content: center;
    gap: 60px;
  }
  .business-card {
    position: relative;
    width: 580px;
    height: 352px;
    display: flex;
    border-radius: 4px;
    overflow: hidden;
    box-shadow: 0 10px 28px rgba(0,0,0,0.22);
  }
  .brand-panel {
    flex: 0 0 352px;
    background: linear-gradient(160deg, var(--card-dark) 0%, var(--card-dark-edge) 100%);
    display: flex;
    align-items: center;
    justify-content: center;
  }
  .brand-block {
    display: flex;
    flex-direction: column;
    align-items: flex-end;
    gap: 10px;
  }
  .brand-lockup {
    display: flex;
    align-items: center;
    gap: 12px;
  }
  .brand-mark {
    width: 18px;
    height: 18px;
    background: var(--brand-blue);
  }
  .brand-name {
    font-family: "Dosis", sans-serif;
    font-weight: 700;
    font-size: 25px;
    letter-spacing: 1px;
    text-transform: uppercase;
    color: var(--brand-grey);
    line-height: 1;
  }
  .brand-tagline {
    font-family: "Dosis", sans-serif;
    font-weight: 600;
    font-size: 12px;
    letter-spacing: 3px;
    text-transform: uppercase;
    color: var(--tagline-blue);
    line-height: 1;
    padding-right: 2px;
  }
  .panel-divider {
    flex: 0 0 8px;
    background: var(--divider-grey);
  }
  .contact-panel {
    flex: 1;
    position: relative;
    background: radial-gradient(circle at 60% 40%, var(--brand-blue) 0%, var(--brand-blue-deep) 100%);
    padding: 46px 22px 0 26px;
    color: var(--text-light);
  }
  .person-name {
    font-family: "Raleway", sans-serif;
    font-weight: 700;
    font-size: 21px;
    letter-spacing: 0.3px;
  }
  .person-role {
    font-family: "Raleway", sans-serif;
    font-weight: 400;
    font-size: 13px;
    color: var(--text-soft);
    margin-top: 6px;
  }
  .contact-list {
    position: absolute;
    left: 26px;
    bottom: 58px;
    list-style: none;
    font-family: "Dosis", sans-serif;
    font-weight: 500;
    font-size: 15px;
    color: var(--text-light);
  }
  .contact-list li + li { margin-top: 26px; }
</style>
</head>
<body>
<main class="canvas">

  <article class="business-card">
    <section class="brand-panel">
      <div class="brand-block">
        <div class="brand-lockup">
          <span class="brand-mark"></span>
          <span class="brand-name">Ironbark Boring Group</span>
        </div>
        <p class="brand-tagline">Western Australia</p>
      </div>
    </section>
    <div class="panel-divider"></div>
    <section class="contact-panel" role="img" aria-label="Blue panel with a subtle tone-on-tone floral damask pattern behind the contact details">
      <h2 class="person-name">Gavin Thorley</h2>
      <p class="person-role">Managing Director</p>
      <ul class="contact-list">
        <li>M. 0481639207</li>
        <li>E. gavin@ibgpty.com.au</li>
      </ul>
    </section>
  </article>

  <article class="business-card">
    <section class="brand-panel">
      <div class="brand-block">
        <div class="brand-lockup">
          <span class="brand-mark"></span>
          <span class="brand-name">Ironbark Boring Group</span>
        </div>
        <p class="brand-tagline">Western Australia</p>
      </div>
    </section>
    <div class="panel-divider"></div>
    <section class="contact-panel" role="img" aria-label="Blue panel with a subtle tone-on-tone floral damask pattern behind the contact details">
      <h2 class="person-name">Martin Thorley</h2>
      <p class="person-role">Director</p>
      <ul class="contact-list">
        <li>M. 0419852637</li>
        <li>E. martin@ibgpty.com.au</li>
      </ul>
    </section>
  </article>

</main>
</body>
</html>
```